Tradeshow display - back drop and matching podium wrap

Looking for a design for a tradeshow display 136.22" x 90.55". and there is approximately 12.25" side panels on each side here (see attached). Needs design for matching podium wrap as well (specs attached).
You can take a look at our website to get a feel on who we are.
www.brindlecrestflow.com
I've added a design I like so you get an idea of what I'm wanting here.
We do not want the Lumora logos on the banner please.
We do water treatment using ozone.

Industry/Entity Type

Agriculture

Requirements
Should not have
• the lumora logos

```html
<!DOCTYPE html>
<html lang="en">
<head>
<meta charset="utf-8">
<title>Brindlecrest Flow – Tradeshow Backdrop and Podium Wrap</title>
<link rel="stylesheet" href="https://fonts.googleapis.com/css2?family=Oswald:wght@500;700&family=Montserrat:wght@500&display=swap">
<style>
  :root {
    --page-bg: #eeeeee;
    --blue-deep: #045a98;
    --blue-bright: #1b79c3;
    --brand-blue: #1a6fb8;
    --white: #ffffff;
    --swoosh-grey: #dedcdd;
    --water-light: #5fb0e6;
    --water-mid: #2f8fd6;
    --step-ring: #9aa8dc;
  }
  * { margin: 0; padding: 0; box-sizing: border-box; }
  html, body { width: 1200px; height: 720px; overflow: hidden; background: var(--page-bg); }
  .canvas { position: relative; width: 1200px; height: 720px; }

  .backdrop, .podium-wrap {
    position: absolute;
    overflow: hidden;
    box-shadow: 0 3px 10px rgba(0,0,0,0.25);
  }
  .backdrop {
    left: 257px; top: 25px; width: 702px; height: 466px;
    background: linear-gradient(90deg, var(--blue-deep), var(--blue-bright));
  }
  .podium-wrap {
    left: 377px; top: 515px; width: 462px; height: 188px;
    background: linear-gradient(90deg, var(--blue-deep), var(--blue-bright));
  }
  .shape-layer { position: absolute; inset: 0; width: 100%; height: 100%; }

  .brand-name {
    position: absolute;
    font-family: "Oswald", sans-serif;
    font-weight: 700;
    line-height: 0.95;
    text-align: center;
  }
  .backdrop .brand-name {
    left: 96px; top: 28px; width: 142px;
    color: var(--brand-blue);
    font-size: 30px;
  }
  .podium-wrap .brand-name {
    left: 181px; top: 48px; width: 100px;
    color: var(--white);
    font-size: 21px;
  }
  .brand-name .brand-sub { display: block; font-size: 0.62em; letter-spacing: 0.12em; }

  .headline {
    position: absolute;
    left: 101px; top: 198px;
    font-family: "Oswald", sans-serif;
    color: var(--white);
    text-transform: uppercase;
    line-height: 1;
  }
  .headline span { display: block; }
  .headline .line-top { font-weight: 700; font-size: 44px; letter-spacing: 0.005em; }
  .headline .line-main { font-weight: 500; font-size: 62px; margin-top: 4px; }
  .headline .line-bottom { font-weight: 700; font-size: 39px; margin-top: 4px; }

  .process-steps { position: absolute; left: 0; top: 0; list-style: none; }
  .step {
    position: absolute;
    left: 300px; width: 302px; height: 56px;
    display: flex; align-items: center; justify-content: flex-end; gap: 10px;
  }
  .step-label {
    font-family: "Montserrat", sans-serif;
    font-weight: 500;
    font-size: 11.5px;
    line-height: 1.12;
    color: var(--white);
    text-align: right;
  }
  .step-badge {
    flex: 0 0 56px; width: 56px; height: 56px;
    border-radius: 50%;
    border: 3px solid var(--step-ring);
    display: flex; align-items: center; justify-content: center;
    position: relative;
  }
  .step-badge::before {
    content: ""; position: absolute; inset: 3px;
    border-radius: 50%; border: 1px dashed var(--white);
  }
  .step-badge span {
    font-family: "Montserrat", sans-serif;
    font-weight: 500; font-size: 11px; line-height: 1.05;
    color: var(--white); text-align: center;
  }

  .site-address {
    position: absolute;
    left: 665px; top: 372px;
    transform-origin: 0 0;
    transform: rotate(-90deg);
    font-family: "Montserrat", sans-serif;
    font-weight: 500;
    font-size: 25px;
    color: var(--white);
    white-space: nowrap;
  }
</style>
</head>
<body>
<main class="canvas">

  <section class="backdrop" aria-label="Tradeshow backdrop">
    <svg class="shape-layer" viewBox="0 0 1447 961" preserveAspectRatio="none">
      <defs>
        <linearGradient id="waterFill" x1="0" y1="0" x2="0" y2="1">
          <stop offset="0" stop-color="var(--water-light)" stop-opacity="0.9"/>
          <stop offset="1" stop-color="var(--water-mid)" stop-opacity="0.85"/>
        </linearGradient>
      </defs>
      <path class="top-swoosh" fill="var(--swoosh-grey)"
            d="M0 0 L632 0 C620 260 520 330 240 375 C90 400 30 450 0 540 Z"/>
      <path class="top-white" fill="var(--white)"
            d="M0 0 L632 0 C632 90 610 150 590 190 C560 250 480 290 300 320 C140 348 60 380 0 470 Z"/>
      <path class="bottom-swoosh" fill="var(--swoosh-grey)"
            d="M0 772 C120 740 220 730 300 735 C430 745 560 840 630 961 L0 961 Z"/>
      <path class="bottom-white" fill="var(--white)"
            d="M0 772 C80 752 160 745 230 752 C360 765 460 850 525 961 L0 961 Z"/>
      <path role="img" aria-label="Clear blue water wave with bubbles" fill="url(#waterFill)"
            d="M420 790 C600 760 760 830 950 770 C1100 725 1200 800 1320 775 C1400 755 1425 690 1447 655 L1447 961 L630 961 C580 880 520 820 420 790 Z"/>
    </svg>

    <div class="brand-name">Brindlecrest<span class="brand-sub">Flow</span></div>

    <h1 class="headline">
      <span class="line-top">Professional</span>
      <span class="line-main">Ozone Water</span>
      <span class="line-bottom">Treatment Services</span>
    </h1>

    <ol class="process-steps">
      <li class="step" style="top:48px"><span class="step-label">Take water<br>analysis</span><span class="step-badge"><span>STEP<br>01</span></span></li>
      <li class="step" style="top:113px"><span class="step-label">Size oxidation needs<br>based on analysis and<br>desired volume</span><span class="step-badge"><span>STEP<br>02</span></span></li>
      <li class="step" style="top:180px"><span class="step-label">Spec and quote<br>system</span><span class="step-badge"><span>STEP<br>03</span></span></li>
      <li class="step" style="top:246px"><span class="step-label">Agreement<br>signed</span><span class="step-badge"><span>STEP<br>04</span></span></li>
      <li class="step" style="top:314px"><span class="step-label">Install system &amp;<br>clean water to<br>desired levels</span><span class="step-badge"><span>STEP<br>05</span></span></li>
    </ol>

    <p class="site-address">brindlecrestflow.com</p>
  </section>

  <section class="podium-wrap" aria-label="Podium wrap">
    <svg class="shape-layer" viewBox="0 0 952 388" preserveAspectRatio="none">
      <defs>
        <linearGradient id="podiumWater" x1="0" y1="0" x2="0" y2="1">
          <stop offset="0" stop-color="var(--water-light)" stop-opacity="0.9"/>
          <stop offset="1" stop-color="var(--water-mid)" stop-opacity="0.85"/>
        </linearGradient>
      </defs>
      <path role="img" aria-label="Clear blue water wave with bubbles" fill="url(#podiumWater)"
            d="M0 290 C150 270 250 330 420 300 C560 275 650 340 800 320 C880 305 920 250 952 230 L952 388 L0 388 Z"/>
    </svg>
    <div class="brand-name">Brindlecrest<span class="brand-sub">Flow</span></div>
  </section>

</main>
</body>
</html>
```